Wine Label for a wine from Tuscany, Italy

We need a wine label for a white and red wine, can be the same label or can be somewhat differentiated with any variation you feel would be good.. These two wines come from Tuscany, Italy. Wine labels from Tuscany Italy tend to be traditional. We are open to traditional looking labels but also more modern, eye catching too. We want to convey a sense of elegance, importance, great wine. I am attaching some examples of labels we like from Tuscany, also a label that was designed for us recently by one of you, which we LOVE. No wine glasses, wine bottles or grapes featured on the label please. We tend to like the white background. No blue please.

Target Market(s)

More women than men purchase wine, but it needs to appeal to both sexes.

Requirements
Must have
• Wine Name: Corte L' or Corte l'
• Type/Varletal: Rosso Toscano (White is Vermentino)
• Vintage (year): 2018
• That is all the text we want on the label, thanks
Nice to have
• Clean, something that makes someone want to grab this wine bottle off the shelf!
Should not have
• Images of Wine glass, wine bottles, grapes
• Do not use the color blue please.

```html
<!DOCTYPE html>
<html lang="it">
<head>
<meta charset="utf-8">
<title>Corte l' — Wine Labels</title>
<link rel="stylesheet" href="https://fonts.googleapis.com/css2?family=Oswald:wght@300;400&display=swap">
<style>
  :root {
    --page-bg: #f1f0ee;
    --panel-black: #0b0b0b;
    --field-white: #f4f4f4;
    --field-red: #d80b17;
    --ink-white: #ffffff;
    --ink-black: #0b0b0b;
  }
  html, body {
    margin: 0;
    padding: 0;
    width: 1200px;
    height: 1143px;
    overflow: hidden;
    background: var(--page-bg);
  }
  .canvas {
    position: relative;
    width: 1200px;
    height: 1143px;
    display: flex;
    justify-content: center;
    align-items: center;
    gap: 60px;
  }
  .label {
    position: relative;
    width: 460px;
    height: 485px;
    display: flex;
    box-shadow: 0 6px 24px rgba(0,0,0,0.12);
  }
  .label__field {
    width: 269px;
    height: 100%;
  }
  .label__rule {
    width: 8px;
    height: 100%;
  }
  .label__gap {
    width: 11px;
    height: 100%;
  }
  .label__panel {
    position: relative;
    flex: 1;
    height: 100%;
    background: var(--panel-black);
    color: var(--ink-white);
    font-family: 'Oswald', sans-serif;
  }
  .label__name {
    position: absolute;
    top: 172px;
    right: 22px;
    margin: 0;
    font-weight: 300;
    font-size: 29px;
    letter-spacing: 3px;
    line-height: 1;
    white-space: nowrap;
  }
  .label__varietal {
    position: absolute;
    top: 214px;
    right: 22px;
    margin: 0;
    font-weight: 300;
    font-size: 13px;
    letter-spacing: 2.5px;
    line-height: 1;
    white-space: nowrap;
  }
  .label__vintage {
    position: absolute;
    bottom: 14px;
    left: 0;
    right: 0;
    margin: 0;
    text-align: center;
    font-weight: 400;
    font-size: 10px;
    letter-spacing: 2px;
  }

  .label--white .label__field,
  .label--white .label__gap { background: var(--field-white); }
  .label--white .label__rule { background: var(--ink-black); }

  .label--red .label__field,
  .label--red .label__gap { background: var(--field-red); }
  .label--red .label__rule { background: var(--ink-white); }
</style>
</head>
<body>
  <main class="canvas">
    <section class="label label--white" aria-label="Vermentino label">
      <div class="label__field"></div>
      <div class="label__rule"></div>
      <div class="label__gap"></div>
      <div class="label__panel">
        <h2 class="label__name">CORTE l'</h2>
        <p class="label__varietal">vermentino</p>
        <p class="label__vintage">2018</p>
      </div>
    </section>

    <section class="label label--red" aria-label="Rosso Toscano label">
      <div class="label__field"></div>
      <div class="label__rule"></div>
      <div class="label__gap"></div>
      <div class="label__panel">
        <h2 class="label__name">CORTE l'</h2>
        <p class="label__varietal">rosso toscano</p>
        <p class="label__vintage">2018</p>
      </div>
    </section>
  </main>
</body>
</html>
```